Recrutering company needs a Roll-Up Design

We need a Roll-Up Design for our company, which is dedicated to personnel selection. We would like the roll-up to feature our logo and the silhouette of the buildings shown in one of the uploaded photos (the one called "BelorquiFestuOre7"). Additionally, we'd like to incorporate the words "Persones," "Talent," and "Èxit" with shadows using the English equivalents instead of the original ones, so: "People" for "Persones," "Talent" for "Talent," and "Success" for "Èxit."

The color of the logo can be changed to red, and the overall design can incorporate this color. As the design is for a roll-up, its essential to take into account a 4cm margin.

```html
<!DOCTYPE html>
<html lang="ca">
<head>
<meta charset="utf-8">
<title>Valdora Roll-Up</title>
<link href="https://fonts.googleapis.com/css2?family=Bebas+Neue&family=Poppins:wght@400;500&display=swap" rel="stylesheet">
<style>
  :root {
    --stage: #e4e4e4;
    --crimson: #c0224e;
    --night: #1b376c;
    --night-deep: #15295a;
    --dusk: #3a5a92;
    --snow: #eef1f8;
    --snow-shade: #dfe5f1;
    --white: #ffffff;
    --reflection: #7d7f85;
  }
  * { margin: 0; padding: 0; box-sizing: border-box; }
  html, body { width: 1200px; height: 2536px; overflow: hidden; }
  body { background: var(--stage); position: relative; }

  .rollup {
    position: absolute;
    left: 80px; top: 48px;
    width: 1040px; height: 2440px;
    overflow: hidden;
    background: linear-gradient(180deg, var(--snow-shade) 0%, var(--snow) 45%, var(--snow-shade) 75%, var(--snow) 100%);
    box-shadow: 0 18px 40px rgba(0,0,0,0.25);
  }

  .night-village {
    position: absolute; left: 0; top: 0;
    width: 1040px; height: 900px;
    background: linear-gradient(180deg, var(--night-deep) 0%, var(--night) 45%, var(--dusk) 72%, #9fb4d8 84%, var(--snow-shade) 100%);
  }

  .brand {
    position: absolute; left: 0; top: 222px; width: 1040px;
    text-align: center; color: var(--white);
    font-family: 'Poppins', sans-serif;
  }
  .brand-name {
    font-size: 52px; font-weight: 500; letter-spacing: 8px; line-height: 1;
  }
  .brand-tagline {
    margin-top: 10px;
    font-size: 21px; font-weight: 500; letter-spacing: 5px; line-height: 1;
  }

  .crimson-wave { position: absolute; left: 0; top: 0; width: 1040px; height: 1100px; }

  .value-icon {
    position: absolute; left: 448px; width: 144px; height: 144px;
  }

  .value-word, .value-shadow {
    position: absolute; left: 0; width: 1040px; text-align: center;
    font-family: 'Bebas Neue', sans-serif; line-height: 1; white-space: nowrap;
  }
  .value-word { color: var(--crimson); z-index: 2; }
  .value-shadow {
    color: var(--reflection); opacity: 0.85; filter: blur(3px);
    transform-origin: 50% 50%; z-index: 1;
  }

  .word-people { top: 1139px; font-size: 134px; }
  .shadow-people { top: 1249px; font-size: 134px; transform: scale(1.8, -1.18); }
  .word-talent { top: 1544px; font-size: 167px; }
  .shadow-talent { top: 1674px; font-size: 167px; transform: scale(1.6, -1.03); }
  .word-success { top: 1985px; font-size: 244px; }
  .shadow-success { top: 2160px; font-size: 167px; transform: scale(1.1, -0.73); }

  .web-band {
    position: absolute; left: 0; top: 2312px; width: 1040px; height: 128px;
    background: var(--crimson); color: var(--white);
    display: flex; align-items: center; justify-content: center;
    font-family: 'Poppins', sans-serif; font-weight: 500;
    font-size: 36px; letter-spacing: 7px;
  }
</style>
</head>
<body>
  <div class="rollup">
    <div class="night-village" role="img" aria-label="Illustration of a snowy village and old factory with a tall chimney under a starry night sky with constellations"></div>

    <div class="brand">
      <div class="brand-name">VALDORA</div>
      <div class="brand-tagline">SELECCIÓ DE TALENT</div>
    </div>

    <svg class="crimson-wave" viewBox="0 0 1040 1100" aria-hidden="true">
      <path fill="var(--crimson)" d="M0,868 C120,815 330,800 560,860 C760,905 900,860 1040,796 L1040,974 C900,1040 700,1045 520,1015 C320,985 150,905 0,875 Z"/>
    </svg>

    <svg class="value-icon" style="top:979px" viewBox="0 0 144 144" aria-hidden="true">
      <circle cx="72" cy="72" r="72" fill="var(--crimson)"/>
      <circle cx="72" cy="72" r="62" fill="none" stroke="var(--white)" stroke-width="4"/>
      <circle cx="72" cy="56" r="15" fill="var(--white)"/>
      <path d="M44,98 a28,24 0 0 1 56,0 z" fill="var(--white)"/>
    </svg>

    <div class="value-shadow shadow-people">PEOPLE</div>
    <div class="value-word word-people">PERSONES</div>

    <svg class="value-icon" style="top:1403px" viewBox="0 0 144 144" aria-hidden="true">
      <circle cx="72" cy="72" r="72" fill="var(--crimson)"/>
      <circle cx="72" cy="72" r="62" fill="none" stroke="var(--white)" stroke-width="4"/>
      <g fill="var(--white)">
        <polygon points="56,36 58,41 63,41 59,44 61,49 56,46 51,49 53,44 49,41 54,41"/>
        <polygon points="72,30 74,35 79,35 75,38 77,43 72,40 67,43 69,38 65,35 70,35"/>
        <polygon points="88,36 90,41 95,41 91,44 93,49 88,46 83,49 85,44 81,41 86,41"/>
        <circle cx="72" cy="64" r="9"/>
        <path d="M40,76 h64 a32,30 0 0 1 -64,0 z"/>
      </g>
      <path d="M58,84 a14,12 0 0 1 28,0" fill="var(--crimson)"/>
    </svg>

    <div class="value-shadow shadow-talent">TALENT</div>
    <div class="value-word word-talent">TALENT</div>

    <svg class="value-icon" style="top:1851px" viewBox="0 0 144 144" aria-hidden="true">
      <circle cx="72" cy="72" r="72" fill="var(--crimson)"/>
      <circle cx="72" cy="72" r="62" fill="none" stroke="var(--white)" stroke-width="4"/>
      <rect x="72" y="42" width="30" height="60" fill="var(--white)"/>
      <path d="M44,72 h22 M56,62 l10,10 l-10,10" fill="none" stroke="var(--white)" stroke-width="6" stroke-linecap="round" stroke-linejoin="round"/>
    </svg>

    <div class="value-shadow shadow-success">SUCCESS</div>
    <div class="value-word word-success">ÈXIT</div>

    <div class="web-band">www.valdoras.com</div>
  </div>
</body>
</html>
```